Bref créative
Business Stationery
Velqis Vantage
Professional
Belinda Hawthorpe
Managing Director
Arvena - Colbrook - Tesmoor
bel@velqisvantage.com
www.velqisvantage.com
Quorn Logo
logo vector file

```html
<!DOCTYPE html>
<html lang="en">
<head>
<meta charset="utf-8">
<title>Velqis Vantage — Business Stationery</title>
<link rel="stylesheet" href="https://fonts.googleapis.com/css2?family=Open+Sans:wght@400;600;700&display=swap">
<style>
  :root {
    --page-bg: #e9eaec;
    --card-bg: #ffffff;
    --green-dark: #2f7d1c;
    --green-mid: #4e9e2a;
    --green-light: #8cc63f;
    --text-dark: #4a4a4a;
    --text-grey: #6d6f71;
    --shadow: rgba(0, 0, 0, 0.18);
  }
  * { margin: 0; padding: 0; box-sizing: border-box; }
  html, body {
    width: 1200px;
    height: 980px;
    overflow: hidden;
    background: var(--page-bg);
    font-family: "Open Sans", Arial, sans-serif;
  }
  .sheet {
    position: relative;
    width: 1200px;
    height: 980px;
  }
  .card {
    position: absolute;
    left: 250px;
    width: 700px;
    height: 400px;
    background: var(--card-bg);
    border-radius: 22px;
    overflow: hidden;
    box-shadow: 0 8px 24px var(--shadow);
  }
  .card--front { top: 70px; }
  .card--back { top: 510px; }

  .front-art {
    position: absolute;
    inset: 0;
    width: 100%;
    height: 100%;
  }

  .brand {
    display: flex;
    align-items: center;
    gap: 12px;
  }
  .brand__dot {
    width: 38px;
    height: 38px;
    border-radius: 50%;
    background: var(--green-mid);
    flex: none;
  }
  .brand__name {
    font-weight: 700;
    font-size: 36px;
    color: var(--text-dark);
    letter-spacing: -0.5px;
    white-space: nowrap;
  }

  .card--front .brand {
    position: absolute;
    left: 44px;
    top: 58px;
  }

  .contact-list {
    position: absolute;
    left: 48px;
    top: 150px;
    list-style: none;
  }
  .contact-list li {
    display: flex;
    align-items: center;
    gap: 10px;
    font-size: 14px;
    color: var(--text-grey);
    line-height: 26px;
    white-space: nowrap;
  }
  .contact-list svg {
    width: 14px;
    height: 14px;
    flex: none;
  }

  .holder {
    position: absolute;
    right: 40px;
    bottom: 34px;
    text-align: right;
  }
  .holder__name {
    font-weight: 700;
    font-size: 17px;
    color: var(--green-mid);
  }
  .holder__role {
    font-size: 13px;
    color: var(--text-grey);
  }

  .card--back {
    display: flex;
    flex-direction: column;
    align-items: center;
    justify-content: center;
    gap: 26px;
  }
  .card--back .brand__dot { width: 46px; height: 46px; }
  .card--back .brand__name { font-size: 40px; }
  .back-web {
    font-size: 14px;
    letter-spacing: 5px;
    color: var(--text-grey);
  }
</style>
</head>
<body>
<main class="sheet">

  <section class="card card--front">
    <svg class="front-art" viewBox="0 0 700 400" aria-hidden="true">
      <defs>
        <linearGradient id="swoosh-green" x1="0" y1="0" x2="1" y2="1">
          <stop offset="0" stop-color="#8cc63f"/>
          <stop offset="0.55" stop-color="#4e9e2a"/>
          <stop offset="1" stop-color="#2f7d1c"/>
        </linearGradient>
        <linearGradient id="band-grey" x1="0" y1="0" x2="1" y2="1">
          <stop offset="0" stop-color="#c7c8ca"/>
          <stop offset="1" stop-color="#7d7f81"/>
        </linearGradient>
      </defs>
      <path d="M250 0 H330 C500 40 630 160 700 300 V330 C610 180 470 55 250 0 Z" fill="url(#band-grey)"/>
      <path d="M330 0 H700 V300 C630 160 500 40 330 0 Z" fill="url(#swoosh-green)"/>
    </svg>

    <div class="brand">
      <span class="brand__dot"></span>
      <span class="brand__name">Velqis Vantage</span>
    </div>

    <ul class="contact-list">
      <li>
        <svg viewBox="0 0 14 14"><path d="M7 1a4 4 0 0 0-4 4c0 3 4 8 4 8s4-5 4-8a4 4 0 0 0-4-4zm0 5.5A1.5 1.5 0 1 1 7 3.5a1.5 1.5 0 0 1 0 3z" fill="var(--green-mid)"/></svg>
        Arvena - Colbrook - Tesmoor
      </li>
      <li>
        <svg viewBox="0 0 14 14"><path d="M3 1h2l1 3-1.5 1a7 7 0 0 0 4.5 4.5L10 8l3 1v2a2 2 0 0 1-2 2C5.5 13 1 8.5 1 3a2 2 0 0 1 2-2z" fill="var(--green-mid)"/></svg>
        00234 80 5550143
      </li>
      <li>
        <svg viewBox="0 0 14 14"><path d="M3 1h2l1 3-1.5 1a7 7 0 0 0 4.5 4.5L10 8l3 1v2a2 2 0 0 1-2 2C5.5 13 1 8.5 1 3a2 2 0 0 1 2-2z" fill="var(--green-mid)"/></svg>
        00234 803 5550178
      </li>
      <li>
        <svg viewBox="0 0 14 14"><rect x="1" y="3" width="12" height="8" rx="1" fill="var(--green-mid)"/><path d="M1.5 3.5 7 8l5.5-4.5" stroke="#fff" stroke-width="1.2" fill="none"/></svg>
        bel@velqisvantage.com
      </li>
      <li>
        <svg viewBox="0 0 14 14"><circle cx="7" cy="7" r="6" fill="var(--green-mid)"/><path d="M1 7h12M7 1c2.5 3 2.5 9 0 12M7 1c-2.5 3-2.5 9 0 12" stroke="#fff" stroke-width="0.9" fill="none"/></svg>
        www.velqisvantage.com
      </li>
    </ul>

    <div class="holder">
      <p class="holder__name">Belinda Hawthorpe</p>
      <p class="holder__role">Managing Director</p>
    </div>
  </section>

  <section class="card card--back">
    <div class="brand">
      <span class="brand__dot"></span>
      <span class="brand__name">Velqis Vantage</span>
    </div>
    <p class="back-web">www.velqisvantage.com</p>
  </section>

</main>
</body>
</html>
```